Etiketten für Weinflasche
Zielgruppe
HANDARBEIT
HAT SEELE.
»80 % gibt uns die Natur vor,
für die restlichen 20 % geben wir alles!«
Volker Brandhuber
Seit über 125 Jahren ist die Rotweinstadt Ingelheim Sitz unseres Familienbetriebes. Im alten Ober-Ingelheimer Schulhaus gelegen, betreiben wir das Weingut in der nunmehr 5. Generation. Unser hoher Qualitätsanspruch und Traditionsbewusstsein wird von Kennern eines guten Weines geschätzt. Zusammen mit der Natur und so schonend wie möglich bewirtschaften wir die rund 15 ha Weinberge in den besten Lagen Ingelheims.
Ganz in der Tradition Karls des Großen, der die Rotweinreben um 800 n. Chr. nach Ingelheim brachte, sind die Spät- und Frühburgunder die Spezialitäten unseres Hauses. Seit 2015 sind wir Träger des „Goldenen Traubenpokals' des Weinkulturmagazins Korkla. Das macht uns stolz und gibt uns Energie. Auch die Rieslinge und die weißen Burgundersorten stehen im Fokus und werden mit viel Gefühl zum Detail gekeltert. Den geselligen Mittelpunkt des Weinguts bildet unser über hundert Jahre alter Pavillon. Er steht symbolisch für uns als gastliche Weinfamilie und vertritt unser Weingut auch nach außen auf unseren Etiketten.
Aufgabenstellung
Ein Wein für FRANKFURTER
Wir möchten für einen führende Marktis-Gruppe in Frankfurt eine Weißwein-Sonderedition entwickeln.
Es soll ein Label sein, womit sich jeder Frankfurter identifizieren kann (Skyline gab es schon mal ist aber nicht ausgeschlossen) und dazu animiert wird die Weinflasche blind zu kaufen.
Die Rebsorte soll auf dem Vorderetikett genannt werden. Es ist ein Grauburgunder oder Grauer Burgunder. Der Wein soll ein schönes Mitbringsel oder auch für den eigenen Genuss sein. Die Flasche wird sich im mittleren Preissegment bewegen +/- 10€ im Verkauf. Zielgruppe 40-65 Jahre alt.
Es gibt drei mögliche Etikettengrößen.
Variante 1: Bestehendes Hollenbach-Etikett mit Streifen (wie in der Anlage)
Variante 2: Vorder- und Rückenetikett mit je 7cm x 7cm oder
Variante 3: Vorderetikett (9cm Breit x 6cm hoch) und Rückenetikett (7cm Breit x 6cm hoch)
Die Rückseite kann ein : gestalterisches Element vom Vorderetikett beinhalten, ist aber durch die gesetzlichen Angaben und den EAN-Code schon ziemlich ausgelastet. Es zum größten Teil um das Vorderetikett.
Die Kapsel am Flaschenhals ist weiß mit gelber Markierung und es gibt eine gelbe Kapsel mit weißer Markierung. Diese ist beiden sind fix, da der Wein schon abgefüllt ist. Es ist eine Burgunderflasche.
Ein Flaschenbild stelle ich zur Verfügung.

```html
<!DOCTYPE html>
<html lang="de">
<head>
<meta charset="utf-8">
<title>Grauer Burgunder – Vorderetikett</title>
<link rel="stylesheet" href="https://fonts.googleapis.com/css2?family=Montserrat:wght@400;500&display=swap">
<style>
  :root {
    --page-bg: #ffffff;
    --gold-edge: #df940f;
    --gold-mid: #f0c132;
    --frame-line: #f2cd6c;
    --paper-white: #ffffff;
    --wine-purple: #8b1a50;
    --dry-gold: #e2a23a;
    --sky-orange: #e8862a;
    --sky-magenta: #b8306a;
    --sky-plum: #8e2550;
  }
  html, body {
    margin: 0;
    width: 1200px;
    height: 1200px;
    overflow: hidden;
    background: var(--page-bg);
  }
  .label {
    position: absolute;
    left: 264px;
    top: 98px;
    width: 672px;
    height: 1004px;
    background:
      linear-gradient(to bottom, transparent 0, transparent 760px, var(--paper-white) 760px),
      linear-gradient(to right, var(--gold-edge) 0%, var(--gold-mid) 50%, var(--gold-edge) 100%);
    font-family: "Montserrat", sans-serif;
    overflow: hidden;
  }
  .label-frame {
    position: absolute;
    inset: 17px;
    border: 2px solid var(--frame-line);
    pointer-events: none;
  }
  .winery-mark {
    position: absolute;
    top: 52px;
    left: 0;
    right: 0;
    text-align: center;
    color: var(--paper-white);
  }
  .winery-dot {
    display: block;
    width: 56px;
    height: 56px;
    margin: 0 auto 20px;
    border-radius: 50%;
    background: var(--paper-white);
  }
  .winery-name {
    display: block;
    font-size: 17px;
    font-weight: 400;
    letter-spacing: 1px;
  }
  .grape-main {
    position: absolute;
    top: 256px;
    left: 0;
    right: 0;
    margin: 0;
    text-align: center;
    color: var(--paper-white);
    font-size: 124px;
    font-weight: 500;
    line-height: 1;
    letter-spacing: -2px;
  }
  .grape-sub {
    position: absolute;
    top: 392px;
    left: 0;
    right: 0;
    text-align: center;
    color: var(--wine-purple);
    font-size: 72px;
    font-weight: 400;
    line-height: 1;
  }
  .skyline {
    position: absolute;
    left: 0;
    top: 540px;
    width: 672px;
    height: 320px;
  }
  .dryness {
    position: absolute;
    top: 898px;
    left: 0;
    right: 0;
    text-align: center;
    color: var(--dry-gold);
    font-size: 25px;
    font-weight: 400;
    letter-spacing: 12px;
    padding-left: 12px;
  }
</style>
</head>
<body>
  <main class="label">
    <div class="label-frame"></div>

    <div class="winery-mark">
      <span class="winery-dot"></span>
      <span class="winery-name">HOLLENBACH</span>
    </div>

    <h1 class="grape-main">GRAUER</h1>
    <div class="grape-sub">BURGUNDER</div>

    <svg class="skyline" role="img" aria-label="Frankfurter Skyline in Aquarell-Tönen von Orange bis Magenta" viewBox="0 0 672 320">
      <defs>
        <linearGradient id="skylineTone" x1="0" y1="0" x2="1" y2="0">
          <stop offset="0" stop-color="var(--sky-plum)"/>
          <stop offset="0.5" stop-color="var(--sky-orange)"/>
          <stop offset="1" stop-color="var(--sky-magenta)"/>
        </linearGradient>
        <linearGradient id="skylineFade" x1="0" y1="0" x2="0" y2="1">
          <stop offset="0" stop-color="#fff" stop-opacity="0.35"/>
          <stop offset="0.45" stop-color="#fff" stop-opacity="1"/>
          <stop offset="1" stop-color="#fff" stop-opacity="1"/>
        </linearGradient>
        <mask id="skylineMask">
          <rect width="672" height="320" fill="url(#skylineFade)"/>
        </mask>
      </defs>
      <path mask="url(#skylineMask)" fill="url(#skylineTone)" opacity="0.9"
            d="M0 150 Q120 130 230 140 Q330 110 420 130 Q540 120 672 140 L672 290
               Q610 310 560 285 Q480 260 410 295 Q330 315 260 285 Q190 265 120 300 Q60 318 0 290 Z"/>
    </svg>

    <div class="dryness">TROCKEN</div>
  </main>
</body>
</html>
```